Stonefield Partners Business Card Design

We are looking for a new business card design, we are not happy with our current design. We are a boutique management consulting firm and our clients are typically fortune 500 companies.

I have attached the current front and back that we have as well as a version of our logo that can be used. I am trying to get a higher resolution version of the logo file to upload to the project.

Target Market(s)

Fortune 500 companies are our primary client base. Financial services, life sciences, pharmaceuticals and telecom companies are

Industry/Entity Type

Management Consulting

Contact Information for Business Card

We are trying to communicate a high degree of professionalism, a somewhat minimalist perhaps with some air of whimsy (without overdoing it). Attached is the current design, front and back as well as logos. I like the current back of the card and assume we will keep the phrase the same.

From a color palette perspective, I prefer to stay with a gray scale as they are today.

Font styles to use
Sans Serif

Colors
1b1b1b
474747
ffffff

Requirements
Must have
• Two sided business card design. File format should be something that can be used outside of Photoshop like MS Publisher so that they can be edited with personal information.
• Font should be calibri or something very similar and should be available within MS Office
Should not have
• No other logos or graphics outside of the logo provided.

```html
<!DOCTYPE html>
<html lang="en">
<head>
<meta charset="utf-8">
<title>Stonefield Partners Business Card</title>
<link rel="stylesheet" href="https://fonts.googleapis.com/css2?family=Carlito:wght@400;700&display=swap">
<style>
  :root {
    --ink: #1b1b1b;
    --graphite: #474747;
    --paper: #ffffff;
    --mist: #d9d9d9;
    --stage: #e9e7e3;
  }
  * { box-sizing: border-box; margin: 0; padding: 0; }
  html, body { width: 1200px; height: 1023px; overflow: hidden; }
  body {
    background: var(--stage);
    font-family: "Carlito", "Calibri", sans-serif;
    display: flex;
    align-items: center;
    justify-content: center;
    gap: 40px;
  }
  .card {
    position: relative;
    width: 540px;
    height: 309px;
    border-radius: 14px;
    overflow: hidden;
    color: var(--paper);
    background: linear-gradient(135deg, var(--graphite) 0%, #2e2e2e 45%, var(--ink) 100%);
    box-shadow: 0 10px 30px rgba(0,0,0,.25);
  }
  /* front */
  .brand {
    position: absolute; left: 26px; top: 26px;
    display: flex; align-items: center; gap: 12px;
  }
  .brand-square {
    width: 62px; height: 62px; border-radius: 6px;
    background: var(--mist);
  }
  .brand-name {
    font-size: 56px; font-weight: 400; line-height: 1; letter-spacing: -0.5px;
  }
  .brand-name sup { font-size: 10px; vertical-align: top; margin-left: 3px; }
  .divider {
    position: absolute; left: 26px; right: 26px; top: 178px;
    height: 1px; background: var(--paper); opacity: .85;
  }
  .person { position: absolute; left: 26px; top: 152px; font-size: 19px; }
  .person strong { font-weight: 700; }
  .person .role { font-size: 12px; }
  .company {
    position: absolute; right: 26px; top: 152px;
    font-size: 19px; font-weight: 700;
  }
  .contact {
    position: absolute; left: 26px; top: 188px;
    font-size: 15px; line-height: 1.5; list-style: none;
  }
  .contact li { display: flex; align-items: center; gap: 7px; }
  .contact svg { width: 12px; height: 12px; fill: var(--paper); flex: none; }
  .contact .office { padding-left: 0; }
  .hq {
    position: absolute; right: 26px; top: 188px;
    font-size: 15px; line-height: 1.5; text-align: right;
  }
  .hq .label { display: flex; justify-content: flex-end; align-items: center; gap: 7px; }
  .hq svg { width: 11px; height: 14px; fill: var(--paper); }
  /* back */
  .card--back { background: linear-gradient(160deg, #262626 0%, var(--ink) 70%); }
  .back-mark {
    position: absolute; left: 0; right: 0; top: 0; bottom: 48px;
    display: flex; align-items: center; justify-content: center;
    font-size: 54px; font-weight: 400;
  }
  .back-band {
    position: absolute; left: 0; right: 0; bottom: 0; height: 48px;
    background: linear-gradient(180deg, #f4f4f4, var(--mist));
    color: var(--ink);
    display: flex; align-items: center; justify-content: center;
    font-size: 15px; letter-spacing: 3px;
  }
</style>
</head>
<body>
  <section class="card card--front">
    <div class="brand">
      <div class="brand-square"></div>
      <div class="brand-name">Stonefield<sup>™</sup></div>
    </div>
    <p class="person"><strong>Mara Ellison</strong>, <span class="role">Managing Director</span></p>
    <p class="company">Stonefield Partners, Inc.</p>
    <div class="divider"></div>
    <ul class="contact">
      <li class="office">Los Angeles Office</li>
      <li><svg viewBox="0 0 24 24"><path d="M6.6 10.8a15 15 0 0 0 6.6 6.6l2.2-2.2a1 1 0 0 1 1-.25 11.4 11.4 0 0 0 3.6.57 1 1 0 0 1 1 1V20a1 1 0 0 1-1 1A17 17 0 0 1 3 4a1 1 0 0 1 1-1h3.5a1 1 0 0 1 1 1c0 1.25.2 2.45.57 3.57a1 1 0 0 1-.25 1z"/></svg>555-014-2273</li>
      <li><svg viewBox="0 0 24 24"><path d="M2 5h20v14H2z M2 5l10 8 10-8" fill="none" stroke="#fff" stroke-width="2"/></svg>mellison@stonefieldpartners.com</li>
    </ul>
    <div class="hq">
      <div class="label">Headquarters <svg viewBox="0 0 12 16"><path d="M6 0a6 6 0 0 0-6 6c0 4.5 6 10 6 10s6-5.5 6-10a6 6 0 0 0-6-6zm0 8.5A2.5 2.5 0 1 1 6 3.5a2.5 2.5 0 0 1 0 5z"/></svg></div>
      <div>218 Harlow Street</div>
      <div>Suite 40, Fairhaven, WA 98000</div>
    </div>
  </section>

  <section class="card card--back">
    <div class="back-mark">Stonefield</div>
    <div class="back-band">www.stonefieldpartners.com</div>
  </section>
</body>
</html>
```